New Property Management Division

We need a flyer designed to discuss our recently launched Property Management division. We are an executive recruiting firm based in Dallas dedicated to the commercial real estate industry. We have historically only worked on investment related positions (acquisitions, development, asset management, etc.) The Property Management division represents our entry into operational positions. We will be placing Property Managers, Leasing Managers, Building Engineers and Property Accountants. The final design should incorporate our existing look and feel - but open to advancing that look as well. I have the logo in vector formats.
Target Market(s)
Commercial Real Estate firms that own (acquire or develop) real estate buildings (retail, office, apartments, industrial, self-storage, etc.).
Industry/Entity Type
Recruitment
Number of Pages Required
1 page
Font styles to use
Other font styles liked:
- We use Calibri a lot
Colors
Designer to choose colors to be used in the design.
Requirements
Must have
- Images of buildings (office, retail, apartments, etc.)
- Description of the types of positions this division will place (Property Managers, Leasing Managers, Building Engineers and Property Accountants)
- Pic and/or bio of the Vice President running property management division (Dale Farrow)
Should not have
- Our clients are professional investors so would not like to see images that are too whimsical.

```html
<!DOCTYPE html>
<html lang="en">
<head>
<meta charset="utf-8">
<title>Halvern Executive Search – Property Management Division</title>
<link rel="stylesheet" href="https://fonts.googleapis.com/css2?family=Oswald:wght@500;600&family=Lato:ital,wght@0,400;0,700;0,900;1,400&family=Montserrat:wght@400;600&display=swap">
<style>
  :root{
    --navy:#1f4e7e;
    --navy-deep:#17395e;
    --blue:#255f96;
    --band-grey:#d6d6d6;
    --charcoal:#3b3b3b;
    --ink:#333;
    --paper:#fff;
    --stage:#eeeeee;
    --headline-pale:#cfe2f7;
  }
  *{box-sizing:border-box;margin:0;padding:0}
  html,body{width:1200px;height:1200px;overflow:hidden;background:var(--stage)}
  .flyer{position:absolute;left:160px;top:30px;width:880px;height:1140px;background:var(--paper);overflow:hidden;box-shadow:0 8px 30px rgba(0,0,0,.15);font-family:"Lato",sans-serif;color:var(--ink)}
  .top-band{position:absolute;left:0;top:40px;width:330px;height:62px;background:var(--navy);clip-path:polygon(0 0,88% 0,100% 100%,0 100%)}
  .hero-photo{position:absolute;left:290px;top:0;width:590px;height:470px;background:linear-gradient(160deg,#6f8fb4 0%,#b9cde6 35%,#3f5f85 70%,#223a57 100%);clip-path:polygon(0 0,100% 0,100% 93%,46% 100%)}
  .brand{position:absolute;left:60px;top:140px;display:flex;align-items:center;gap:14px}
  .brand-mark{width:34px;height:34px;background:var(--navy)}
  .brand-name{font-family:"Lato",sans-serif;font-weight:400;color:var(--navy-deep);font-size:30px;letter-spacing:7px;line-height:1}
  .brand-name small{display:block;font-size:13px;letter-spacing:4px;margin-top:4px}
  .headline-block{position:absolute;left:0;top:232px;width:560px;height:200px;background:linear-gradient(135deg,var(--navy-deep),var(--blue));clip-path:polygon(0 0,82% 0,100% 100%,0 100%);padding:32px 0 0 50px}
  .headline-block .line1{font-family:"Oswald",sans-serif;font-weight:600;font-size:52px;color:var(--headline-pale);line-height:1;text-transform:uppercase}
  .headline-block .line2{font-family:"Oswald",sans-serif;font-weight:500;font-size:36px;color:var(--paper);line-height:1.1;text-transform:uppercase}
  .headline-block .line3{font-family:"Montserrat",sans-serif;font-weight:400;font-size:30px;color:var(--paper);line-height:1.15;text-transform:uppercase;letter-spacing:1px}
  .intro{position:absolute;left:80px;top:468px;width:720px;text-align:center;font-style:italic;font-size:16px;line-height:1.35}
  .division{position:absolute;left:0;top:548px;width:880px;height:300px;background:var(--band-grey)}
  .division-lead{margin:22px auto 0;width:720px;text-align:center;font-family:"Montserrat",sans-serif;font-size:18px;line-height:1.35}
  .roles{display:flex;justify-content:space-between;margin-top:26px;padding:0 30px;list-style:none}
  .role{display:flex;flex-direction:column;align-items:center;width:200px}
  .role-icon{width:62px;height:62px;border-radius:50%;background:var(--navy);border:3px solid var(--paper);box-shadow:0 2px 4px rgba(0,0,0,.25);display:flex;align-items:center;justify-content:center}
  .role-name{margin-top:14px;font-family:"Montserrat",sans-serif;font-weight:600;font-size:14px;text-transform:uppercase;text-align:center;white-space:nowrap}
  .rule{position:absolute;left:0;top:848px;width:880px;height:9px;background:var(--blue)}
  .portrait{position:absolute;left:595px;top:785px;width:250px;height:280px;background:linear-gradient(180deg,#c9c2bb 0%,#8a8a8a 40%,#5a5d60 100%);border-radius:110px 110px 0 0}
  .bio{position:absolute;left:60px;top:885px;width:480px}
  .bio-name{color:var(--blue);font-weight:700;font-size:20px}
  .bio-text{font-size:16px;line-height:1.3;text-align:justify;margin-top:6px}
  .contact{position:absolute;left:0;top:1020px;width:500px;height:120px;background:var(--blue);clip-path:polygon(0 0,90% 0,100% 100%,0 100%);color:var(--paper);padding:22px 0 0 50px}
  .contact-row{display:flex;align-items:center;gap:14px}
  .contact-email{font-size:18px}
  .contact-phone{font-size:34px;font-family:"Montserrat",sans-serif;margin-top:4px}
  .web-band{position:absolute;left:470px;top:1050px;width:410px;height:90px;background:var(--charcoal);color:var(--paper);display:flex;align-items:center;gap:14px;padding-left:60px;font-size:22px;letter-spacing:.5px}
</style>
</head>
<body>
<main class="flyer">
  <div class="top-band"></div>
  <div class="hero-photo" role="img" aria-label="Photo looking up at glass office towers against a blue cloudy sky"></div>

  <div class="brand">
    <span class="brand-mark"></span>
    <span class="brand-name">HALVERN<small>executive search</small></span>
  </div>

  <div class="headline-block">
    <div class="line1">Exclusively</div>
    <div class="line2">Serving the Commercial</div>
    <div class="line3">Real Estate Industry</div>
  </div>

  <p class="intro">We are an executive recruiting firm based in Dallas dedicated to the commercial real estate industry. We have historically only worked on investment related positions (acquisitions, development, asset management, etc.)</p>

  <section class="division">
    <p class="division-lead">The Property Management division represents our entry into operational positions. We will be placing:</p>
    <ul class="roles">
      <li class="role">
        <span class="role-icon"><svg width="34" height="34" viewBox="0 0 34 34" fill="#fff"><circle cx="11" cy="7" r="4"/><rect x="7" y="12" width="8" height="16" rx="2"/><rect x="18" y="6" width="11" height="22"/></svg></span>
        <span class="role-name">Property Managers</span>
      </li>
      <li class="role">
        <span class="role-icon"><svg width="34" height="34" viewBox="0 0 34 34" fill="#fff"><path d="M8 12a9 9 0 0 1 18 0z"/><rect x="6" y="12" width="22" height="2"/><circle cx="17" cy="18" r="4"/><path d="M7 32c0-7 5-9 10-9s10 2 10 9z"/></svg></span>
        <span class="role-name">Building Engineers</span>
      </li>
      <li class="role">
        <span class="role-icon"><svg width="34" height="34" viewBox="0 0 34 34" fill="none" stroke="#fff" stroke-width="2"><rect x="14" y="4" width="16" height="11" rx="2"/><circle cx="10" cy="17" r="3.5" fill="#fff"/><path d="M4 30c0-5 3-7 6-7s6 2 6 7z" fill="#fff"/></svg></span>
        <span class="role-name">Leasing Managers</span>
      </li>
      <li class="role">
        <span class="role-icon"><svg width="34" height="34" viewBox="0 0 34 34" fill="none" stroke="#fff" stroke-width="2.2"><path d="M6 16 17 6l11 10"/><path d="M9 14v11h16V14"/><path d="M4 28c6 0 8-3 13-3s6 3 13 3"/></svg></span>
        <span class="role-name">Property Accountants</span>
      </li>
    </ul>
  </section>
  <div class="rule"></div>

  <div class="portrait" role="img" aria-label="Portrait of Dale Farrow, Vice President of the Property Management division, in a grey suit with arms crossed"></div>

  <section class="bio">
    <h2 class="bio-name">Dale Farrow</h2>
    <p class="bio-text">Lorem Ipsum is simply dummy text of the printing and typesetting industry. Lorem Ipsum has been the industry's standard dummy text ever since the 1500s, when an unknown printer took a galley of type and scrambled it to make a type specimen book.</p>
  </section>

  <footer>
    <div class="contact">
      <div class="contact-row contact-email">
        <svg width="22" height="22" viewBox="0 0 22 22"><circle cx="11" cy="11" r="11" fill="#fff"/><rect x="5" y="7" width="12" height="8" fill="none" stroke="#255f96" stroke-width="1.5"/><path d="M5 7l6 5 6-5" fill="none" stroke="#255f96" stroke-width="1.5"/></svg>
        info@halvernsearch.com
      </div>
      <div class="contact-row contact-phone">
        <svg width="22" height="22" viewBox="0 0 22 22"><circle cx="11" cy="11" r="11" fill="#fff"/><path d="M7 6c1-1 2 0 3 2s-1 2 0 3 2 2 3 2 1-2 3 0 0 3-2 3C10 16 6 12 7 6z" fill="#255f96"/></svg>
        214-555-0148
      </div>
    </div>
    <div class="web-band">
      <svg width="20" height="20" viewBox="0 0 20 20" fill="none" stroke="#fff" stroke-width="1.5"><circle cx="10" cy="10" r="8"/><ellipse cx="10" cy="10" rx="3.5" ry="8"/><path d="M2 10h16"/></svg>
      www.halvernsearch.com
    </div>
  </footer>
</main>
</body>
</html>
```